Video Editing Website - Wordpress Design Project

Hi There
I am setting up a Tribute Funeral Video and Home Video Editing Website for my Company. "Cut My Reel". This is to assist people with putting together their Videos and Photos with music to show at a Funeral or for Family Memories. I already have a domain www.cutmyreel.com.au, but I have no host yet.

Some websites that already do this are http://www.farewellclips.com.au/tributes, http://www.familyfilmcrafting.com.au/services/funeral-tribute-videos.html, and http://www.memorialslideworks.com.au/
These are examples not to cpy, but to get an idea of what I am offering so you can design accordingly.

I have a logo which is attached. You will see that the logo is mainly blue, so I would appreciate a website with that colour on the pages, but not ALL over the page.

I would like to upload videos occasionally from clipnest.com so I would appreciate that option incorporated.

Thank you lots.
Gareth

Target Market(s)

Families predominately in the 25-60 age range

Industry/Entity Type

It Company

Requirements
Must have
• *Ability to upload Videos from clipnest.com
*Ability for me to edit the content whenever I need to
*A contact page to send email messages to me

```html
<!DOCTYPE html>
<html lang="en">
<head>
<meta charset="utf-8">
<title>Cut My Reel</title>
<link href="https://fonts.googleapis.com/css2?family=Source+Sans+3:wght@400;600&display=swap" rel="stylesheet">
<style>
:root{
  --blue:#2a4ea8;
  --blue-dark:#1f3f92;
  --blue-light:#3b67c4;
  --text:#444;
  --heading:#333;
  --footer:#3a3a3a;
  --footer-bottom:#2b2b2b;
  --footer-text:#d8d8d8;
  --gray-bg:#f3f3f3;
}
*{box-sizing:border-box;margin:0;padding:0}
html,body{width:723px;height:1200px;overflow:hidden;background:#fff}
body{position:relative;font-family:"Source Sans 3",Arial,sans-serif;color:var(--text)}
.abs{position:absolute}
.brand{left:52px;top:30px;display:flex;align-items:center;gap:8px}
.brand-mark{width:28px;height:28px;border-radius:50%;background:var(--blue)}
.brand-name{font-size:22px;font-weight:600;color:var(--blue)}
.call{right:53px;top:24px;font-size:14px;font-weight:600;color:#333}
.search{left:534px;top:50px;width:136px;height:21px;border:1px solid #ccc;border-radius:3px;font-size:8px;color:#aaa;padding:4px 5px}
.search svg{position:absolute;right:6px;top:5px}
.nav{left:0;top:85px;width:723px;height:29px;background:linear-gradient(#3a66c2,#244a9e);display:flex;padding-left:45px}
.nav a{color:#fff;font-size:10px;text-decoration:none;padding:0 15px;line-height:29px;border-right:1px solid rgba(255,255,255,.25)}
.nav a:last-child{border-right:0}
.hero{left:0;top:114px;width:723px;height:293px;background:linear-gradient(#9cc3ea 0%,#c9dcef 50%,#8a8a70 85%,#b5a878 100%)}
.caption{left:52px;top:310px;width:255px;height:68px;background:rgba(60,60,60,.72);color:#fff;padding:9px 11px}
.caption h2{font-size:12.5px;font-weight:600;margin-bottom:4px}
.caption p{font-size:9px;line-height:15px}
.dots{left:641px;top:387px;display:flex;gap:2px}
.dots i{width:6px;height:6px;border-radius:50%;background:#333;border:1px solid #fff}
.dots i:first-child{background:#fff;border-color:#333}
.welcome{left:0;top:418px;width:723px;text-align:center}
.welcome h1{font-size:16px;font-weight:600;color:var(--heading);margin-bottom:9px}
.welcome p{font-size:9.5px;line-height:18px;width:560px;margin:0 auto}
.btn{left:321px;top:487px;width:74px;height:23px;background:linear-gradient(#444,#111);color:#fff;font-size:9px;text-align:center;line-height:23px;border-radius:3px}
.divider{left:90px;top:523px;width:543px;height:1px;background:linear-gradient(90deg,transparent,#ddd,transparent)}
.feature{top:545px;width:200px;text-align:center}
.halo{width:92px;height:92px;border-radius:50%;background:#eee;margin:0 auto;display:flex;align-items:center;justify-content:center}
.circle{width:78px;height:78px;border-radius:50%;background:var(--blue);display:flex;align-items:center;justify-content:center}
.feature h3{font-size:13px;font-weight:600;color:var(--heading);margin:6px 0 4px}
.feature p{font-size:9px;line-height:13px;width:150px;margin:0 auto}
.card{top:733px;width:185px;height:112px;background:linear-gradient(#3460bb,#24479c);border-radius:2px;color:#fff}
.card-head{height:42px;display:flex;align-items:center;gap:10px;padding-left:12px;border-bottom:1px solid rgba(255,255,255,.2);font-size:12.5px;font-weight:600}
.card p{font-size:8px;line-height:13px;padding:7px 12px 0}
.card .more{position:absolute;right:15px;bottom:12px;font-size:8px;display:flex;align-items:center;gap:4px}
.projects{left:0;top:868px;width:723px;height:170px;background:var(--gray-bg)}
.projects h2{position:absolute;left:52px;top:8px;font-size:14.5px;font-weight:600;color:var(--heading)}
.proj{top:897px;width:185px}
.proj .img{height:84px;position:relative}
.proj .play{position:absolute;left:78px;top:27px;width:28px;height:28px;border-radius:50%;background:rgba(255,255,255,.6);border:2px solid rgba(255,255,255,.9)}
.proj p{font-size:8px;line-height:13px;margin-top:12px;color:#444}
.footer{left:0;top:1038px;width:723px;height:130px;background:var(--footer)}
.fcol{top:1050px;color:var(--footer-text)}
.fcol h4{font-size:11px;font-weight:400;color:#fff;margin-bottom:4px}
.fcol li{list-style:none;font-size:8px;line-height:17.5px}
.bottom{left:0;top:1168px;width:723px;height:32px;background:var(--footer-bottom)}
.copy{left:57px;top:1179px;font-size:8px;color:var(--footer-text)}
.social{left:547px;top:1175px;display:flex;gap:12px}
.social i{width:18px;height:18px;border-radius:50%;background:#2d6fb8}
</style>
</head>
<body>
<div class="abs brand"><span class="brand-mark"></span><span class="brand-name">Cut My Reel</span></div>
<div class="abs call">Call : +67 512 3408</div>
<div class="abs search">Search..<svg width="9" height="9" viewBox="0 0 10 10"><circle cx="4" cy="4" r="3" fill="none" stroke="#999" stroke-width="1.4"/><line x1="6.2" y1="6.2" x2="9" y2="9" stroke="#999" stroke-width="1.4"/></svg></div>
<nav class="abs nav"><a>HOME</a><a>ABOUT US</a><a>SERVICES</a><a>PACKAGES</a><a>BOOKING FORM</a><a>SAMPLES</a><a>TERMS</a><a>FAQ</a><a>CONTACT</a></nav>
<div class="abs hero" role="img" aria-label="Family of three generations walking hand in hand across a grassy field under a blue sky"></div>
<div class="abs caption"><h2>Amet dolor sit tation ullamcorper</h2><p>Donec id ante magna. Nullam sollicitudin, ipsum vel hendrerit aliquam, nisi sapien pellentesque odio.</p></div>
<div class="abs dots"><i></i><i></i><i></i><i></i></div>
<section class="abs welcome"><h1>Welcome to our Website</h1><p>Claritas est etiam processus dynamicus, qui sequitur mutationem consuetudium lectorum. Mirum est notare quam littera gothica, quam nunc putamus parum claram, anteposuerit litterarum formas humanitatis per seacula quarta decima et quinta decima.</p></section>
<div class="abs btn">READ MORE</div>
<div class="abs divider"></div>

<div class="abs feature" style="left:55px"><div class="halo"><div class="circle"><svg width="30" height="28" viewBox="0 0 30 28"><rect x="2" y="11" width="26" height="15" fill="#fff"/><path d="M2 9 L26 3 L27 7 L3 13Z" fill="#fff"/></svg></div></div><h3>Upload Video</h3><p>Lorem ipsum dolor sit amet adipis ing elit.Morbi ut elipsum tristique acc umsan. Morbi ut elit utipsum tristiquea Pellentesque habitant morbi.</p></div>
<div class="abs feature" style="left:258px"><div class="halo"><div class="circle"><svg width="26" height="30" viewBox="0 0 26 30"><rect x="2" y="2" width="22" height="26" fill="none" stroke="#fff" stroke-width="2"/><line x1="7" y1="2" x2="7" y2="28" stroke="#fff" stroke-width="1.5"/><line x1="19" y1="2" x2="19" y2="28" stroke="#fff" stroke-width="1.5"/><line x1="7" y1="15" x2="19" y2="15" stroke="#fff" stroke-width="1.5"/></svg></div></div><h3>Upload Photos</h3><p>Lorem ipsum dolor sit amet adipis ing elit.Morbi ut elipsum tristique acc umsan. Morbi ut elit utipsum tristiquea Pellentesque habitant morbi.</p></div>
<div class="abs feature" style="left:458px"><div class="halo"><div class="circle"><svg width="32" height="32" viewBox="0 0 32 32"><circle cx="14" cy="14" r="11" fill="none" stroke="#fff" stroke-width="2.5"/><line x1="3" y1="14" x2="25" y2="14" stroke="#fff" stroke-width="2"/><ellipse cx="14" cy="14" rx="5" ry="11" fill="none" stroke="#fff" stroke-width="2"/><path d="M18 16 L30 22 L24 23 L27 30 L24 31 L21 25 L18 28Z" fill="#fff" stroke="#2a4ea8"/></svg></div></div><h3>FAQ</h3><p>Lorem ipsum dolor sit amet adipis ing elit.Morbi ut elipsum tristique acc umsan. Morbi ut elit utipsum tristiquea Pellentesque habitant morbi.</p></div>

<div class="abs card" style="left:52px"><div class="card-head"><svg width="20" height="20" viewBox="0 0 20 20"><circle cx="10" cy="10" r="6" fill="none" stroke="#fff" stroke-width="4" stroke-dasharray="3 2"/><circle cx="10" cy="10" r="2.5" fill="#fff"/></svg>Package Details</div><p>Vivamus vel eros eget maigna volutpat sagit tis. Nulla faucibus nibh a magna tincidunt ac cumsan</p><span class="more">Click Here <svg width="10" height="10" viewBox="0 0 10 10"><circle cx="5" cy="5" r="5" fill="#fff"/><path d="M3 5h4M5 3l2 2-2 2" stroke="#2a4ea8" fill="none" stroke-width="1.3"/></svg></span></div>
<div class="abs card" style="left:269px"><div class="card-head"><svg width="22" height="20" viewBox="0 0 22 20"><rect x="1" y="8" width="19" height="11" fill="#fff"/><path d="M1 6 L18 1 L19 4 L2 9Z" fill="#fff"/></svg>Funeral Tribute Video</div><p>Vivamus vel eros eget maigna volutpat sagit tis. Nulla faucibus nibh a magna tincidunt ac cumsan</p><span class="more">Click Here <svg width="10" height="10" viewBox="0 0 10 10"><circle cx="5" cy="5" r="5" fill="#fff"/><path d="M3 5h4M5 3l2 2-2 2" stroke="#2a4ea8" fill="none" stroke-width="1.3"/></svg></span></div>
<div class="abs card" style="left:486px"><div class="card-head"><svg width="28" height="24" viewBox="0 0 28 24"><path d="M1 12 L27 1 L20 23 L13 15Z M13 15 L27 1" fill="none" stroke="#fff" stroke-width="1.6"/></svg>Helpful Tips</div><p>Vivamus vel eros eget maigna volutpat sagit tis. Nulla faucibus nibh a magna tincidunt ac cumsan</p><span class="more">Click Here <svg width="10" height="10" viewBox="0 0 10 10"><circle cx="5" cy="5" r="5" fill="#fff"/><path d="M3 5h4M5 3l2 2-2 2" stroke="#2a4ea8" fill="none" stroke-width="1.3"/></svg></span></div>

<section class="abs projects"><h2>Latest Projects</h2></section>
<div class="abs proj" style="left:52px"><div class="img" role="img" aria-label="Family walking along the beach by the sea" style="background:linear-gradient(#7fb3d8,#4d87b3 55%,#d8d2c4)"><span class="play"></span></div><p>Lorem ipsum dolor sit amet, consectetur adipisicin g elit, sed do eiusmod tempor.</p></div>
<div class="abs proj" style="left:272px"><div class="img" role="img" aria-label="Smiling family outdoors under a bright blue sky" style="background:linear-gradient(#2f6fc4,#5a92d6 50%,#d49a5c)"><span class="play"></span></div><p>Lorem ipsum dolor sit amet, consectetur adipisicin g elit, sed do eiusmod tempor.</p></div>
<div class="abs proj" style="left:490px"><div class="img" role="img" aria-label="Couple running with their daughter through a summer meadow" style="background:linear-gradient(#8fbde8,#cfe2f2 55%,#8aa656)"><span class="play"></span></div><p>Lorem ipsum dolor sit amet, consectetur adipisicin g elit, sed do eiusmod tempor.</p></div>

<footer class="abs footer"></footer>
<div class="abs fcol" style="left:52px"><h4>FeedbacK Portal</h4><ul><li>Team Portal</li><li>FeedbacK Exchange</li><li>Proin sit amet nulla</li><li>Consectetur adipiscing</li><li>Malesuada ullamcor</li></ul></div>
<div class="abs fcol" style="left:185px"><h4>Who We Are</h4><ul><li>About us</li><li>Eoidem temper</li><li>Consectetur adiping</li><li>Sed id purus vel</li><li>Lorem ipsum</li></ul></div>
<div class="abs fcol" style="left:301px"><h4>Outreach</h4><ul><li>Sed scelerisque</li><li>Consectetur adipisicing</li><li>FeedbacK Attends</li><li>Venture eoim2013</li><li>Ready to Tee Up First of Three</li></ul></div>
<div class="abs fcol" style="left:450px"><h4>Links</h4><ul><li>About us</li><li>Consectetur adicing</li><li>Consectetur adicing</li><li>Sed id purus vel</li><li>Lorem ipsum</li></ul></div>
<div class="abs fcol" style="left:576px"><h4>Other Information</h4><ul><li>Privacy Policy</li><li>Terms &amp; Conditions</li></ul></div>
<div class="abs bottom"></div>
<div class="abs copy">Copyrights 2013. All Rights Reserved.</div>
<div class="abs social"><i></i><i></i><i></i><i></i></div>
</body>
</html>
```